Web and Logo Design - Investing Website

Financial website, so needs to be clean and professional. I like vector images that are simple and professional (data, investing) but do not overpower the website. Will need to show off the charts to emphasize portfolio’s performance. Should be mainly blue and white (does not have to be the blue tones selected). Homepage should have a section where it shows off the three portfolios with a quick summary (see content file) and performance graph (see performance charts file) - with a "learn more" link.

Homepage Header links - Strategies; Monthly Updates; FAQ; Signup; Login

Pages needed:
Homepage
Articles/Blog Main Page
Article Layout Template
Dashboard Template (see Dashboard information file)

Sample designs i like: https://www.plimvaro.io/ - https://www.brastekin.com/ - https://www.holvendarquist.com/

Industry/Entity Type

Finance - Investing

Number of Pages Required

4 page

Colors
0054AA
0677BA
7BADD7
CADEEF
E8F1F8

Requirements
Should not have
• Generic pictures of people

```html
<!DOCTYPE html>
<html lang="en">
<head>
<meta charset="utf-8">
<title>Blog Post Article Pages</title>
<link rel="stylesheet" href="https://fonts.googleapis.com/css2?family=Barlow:wght@400;500;600;700;800&family=Montserrat:wght@400;500;600&display=swap">
<style>
:root{
  --board:#cfdfe6;
  --title:#78a8cf;
  --navy:#0054aa;
  --blue:#0677ba;
  --sky:#7badd7;
  --mist:#cadeef;
  --ice:#e8f1f8;
  --ink:#4a4f57;
  --white:#ffffff;
  --foot-top:#184f9a;
  --foot-bottom:#0f67b5;
}
*{box-sizing:border-box;margin:0;padding:0}
html,body{width:1158px;height:1200px;overflow:hidden;background:var(--board)}
.board{position:relative;width:1158px;height:1200px;background:var(--board)}
.board-title{position:absolute;left:0;top:44px;width:1158px;text-align:center;font-family:"Barlow",sans-serif;font-weight:700;font-size:73px;letter-spacing:1px;color:var(--title);line-height:1}
.page{position:absolute;top:173px;width:498px;background:var(--white);overflow:hidden;font-family:"Montserrat",sans-serif;color:var(--ink)}
.page--article{left:50px;height:987px}
.page--listing{left:605px;height:954px}
.abs{position:absolute}
.site-header{position:absolute;left:0;top:0;width:100%;height:34px;border-bottom:1px solid var(--ice);background:var(--white);z-index:2}
.brand{position:absolute;display:flex;align-items:center;gap:4px}
.brand-dot{width:15px;height:15px;border-radius:50%;background:var(--navy);flex:none}
.brand-name{font-family:"Barlow",sans-serif;font-weight:500;font-size:8.4px;line-height:7.6px;color:var(--navy);letter-spacing:.2px;text-transform:uppercase}
.site-header .brand{left:47px;top:10px}
.nav-link{position:absolute;top:15px;font-size:5px;font-weight:600;color:var(--navy);letter-spacing:.2px}
.btn{position:absolute;top:12px;width:37px;height:14px;font-size:4.6px;font-weight:600;display:flex;align-items:center;justify-content:center;border-radius:1px}
.btn--ghost{left:360px;border:1px solid var(--blue);color:var(--navy)}
.btn--solid{left:400px;background:var(--blue);color:var(--white)}
.art{position:absolute;border-radius:2px}
.date-pill{position:absolute;background:var(--sky);color:var(--white);font-family:"Barlow",sans-serif;font-weight:500;border-radius:8px;display:flex;align-items:center;justify-content:center}
.post-title{position:absolute;font-family:"Barlow",sans-serif;font-weight:600;color:var(--navy);line-height:14.5px}
.byline{position:absolute;display:flex;align-items:center;font-family:"Barlow",sans-serif;font-size:7px;color:var(--blue)}
.share{display:flex;gap:2px;margin-left:11px}
.share span{width:8px;height:8px;border-radius:50%;background:var(--navy)}
.copy{position:absolute;font-size:6.2px;line-height:11.1px;color:var(--ink)}
.copy p{margin-bottom:6px}
.section-head{position:absolute;font-family:"Barlow",sans-serif;font-weight:600;font-size:10px;color:var(--navy)}
.footer-wave{position:absolute;left:0;width:498px}
.footer-brand{position:absolute;left:63px}
.footer-brand .brand-name{color:var(--white)}
.footer-brand .brand-dot{background:var(--white)}
.footer-social{position:absolute;left:67px;display:flex;gap:3px}
.footer-social span{width:10px;height:10px;border-radius:50%;background:var(--white)}
.footer-divider{position:absolute;width:1px;height:89px;background:rgba(255,255,255,.18)}
.footer-col{position:absolute;color:var(--white);font-family:"Barlow",sans-serif}
.footer-col h4{font-size:7px;font-weight:600;border-left:1px solid var(--white);margin-left:-12px;padding-left:11px;line-height:8px;margin-bottom:3px}
.footer-col li{list-style:none;font-size:4.9px;line-height:9.6px;opacity:.9}
.hero-title{position:absolute;left:50px;top:88px;font-family:"Barlow",sans-serif;font-size:20.5px;font-weight:400;color:var(--navy)}
.hero-title strong{font-weight:700}
.hero-sub{position:absolute;left:50px;top:118px;font-size:6.6px;line-height:10.5px;color:var(--ink)}
</style>
</head>
<body>
<div class="board">
  <h1 class="board-title">BLOG POST ARTICLE PAGES</h1>

  <!-- Article template page -->
  <section class="page page--article">
    <svg class="abs" style="left:0;top:34px" width="498" height="190" viewBox="0 0 498 190">
      <defs><linearGradient id="heroA" x1="0" y1="0" x2="0" y2="1"><stop offset="0" stop-color="#eef5fb"/><stop offset="1" stop-color="#f6fafd"/></linearGradient></defs>
      <path d="M0 0H498V160C430 170 380 190 300 176C210 160 130 140 60 158C30 166 10 168 0 166Z" fill="url(#heroA)"/>
      <path d="M0 166C40 175 80 185 130 182C210 176 260 150 340 160C410 168 460 150 498 146V190H0Z" fill="#fff"/>
    </svg>
    <header class="site-header">
      <div class="brand"><span class="brand-dot"></span><span class="brand-name">Northfold<br>Portfolio</span></div>
      <span class="nav-link" style="left:178px">STRATEGIES</span>
      <span class="nav-link" style="left:231px">MONTHLY UPDATES</span>
      <span class="nav-link" style="left:303px">FAQ</span>
      <span class="btn btn--ghost">SIGN UP</span>
      <span class="btn btn--solid">LOGIN</span>
    </header>

    <div class="art" role="img" aria-label="Isometric illustration of a data dashboard platform with charts and connected modules" style="left:57px;top:61px;width:381px;height:191px;border:1px solid var(--mist);background:radial-gradient(ellipse at 50% 50%,#1b4f8f 0 18%,#9cc3e6 32%,#eef5fb 60%,#f8fbfe 100%)"></div>
    <div class="date-pill" style="left:66px;top:245px;width:67px;height:13px;font-size:6.6px">05 SEP 2021</div>

    <h2 class="post-title" style="left:75px;top:272px;width:360px;font-size:11.3px">Sed ut perspiciatis unde omnis iste natus error sit voluptatem accu-<br>santium doloremque laudantium, totam rem aperiam</h2>
    <div class="byline" style="left:75px;top:306px">By Elias Brennard MD<span class="share"><span></span><span></span><span></span></span></div>

    <div class="copy" style="left:73px;top:328px;width:366px">
      <p>Aorem ipsum dolor sit amet, consectetur adipiscing elit, sed do eiusmod tempor incididunt ut labore et dolore magna liqua. Ut enim ad minim veniam, quis nostrud exercitation ullamco laboris nisi ut aliquip ex ea commodo consequat. Duis aute irure dolor in reprehenderit in voluptate velit esse cillum dolore eu fugiat</p>
      <p>Sed ut perspiciatis unde omnis iste natus error sit voluptatem accusantium doloremque laudantium, totam rem aperiam, eaque ipsa quae ab illo inventore veritatis et quasi architecto beatae vitae dicta sunt explicabo. Nemo enim ipsam voluptatem quia voluptas sit aspernatur aut odit aut fugit, sed quia consequuntur magni dolores eos qui ratione voluptatem sequi nesciunt. Neque porro quisquam est, qui dolorem ipsum quia dolor sit amet, consectetur,</p>
      <p>Adipisci velit, sed quia non numquam eius modi tempora incidunt ut labore et dolore magnam aliquam quaerat voluptatem. Ut enim ad minima veniam, quis nostrum exercitationem ullam corporis suscipit laboriosam, nisi ut aliquid ex ea commodi consequatur? Quis autem vel eum</p>
    </div>

    <h3 class="section-head" style="left:73px;top:470px">Aoloremque laudantium, totam rem aperiam</h3>
    <div class="copy" style="left:72px;top:490px;width:366px">
      <p>Aorem ipsum dolor sit amet, consectetur adipiscing elit, sed do eiusmod tempor incididunt ut labore et dolore magna liqua. Ut enim ad minim veniam, quis nostrud exercitation ullamco laboris nisi ut aliquip ex ea commodo consequat. Duis aute irure dolor in reprehenderit in voluptate velit esse cillum dolore eu fugiat</p>
      <p>Sed ut perspiciatis unde omnis iste natus error sit voluptatem accusantium doloremque laudantium, totam rem aperiam, eaque ipsa quae ab illo inventore veritatis et quasi architecto beatae vitae dicta sunt explicabo. Nemo enim ipsam voluptatem quia voluptas sit aspernatur aut odit aut fugit, sed quia consequuntur magni dolores eos qui ratione voluptatem sequi nesciunt. Neque porro quisquam est, qui dolorem ipsum quia dolor sit amet, consectetur,</p>
    </div>

    <h3 class="section-head" style="left:71px;top:597px">Sed ut perspiciatis unde omnis iste</h3>
    <div class="copy" style="left:71px;top:617px;width:214px">
      <p>Aorem ipsum dolor sit amet, consectetur adipiscing elit, sed do eiusmod tempor incididunt ut labore et dolore magna liqua. Ut enim ad minim veniam, quis nostrud exercitation ullamco laboris nisi ut aliquip ex ea commodo consequat. Duis aute irure dolor in reprehenderit in voluptate velit esse cillum dolore eu fugiat</p>
      <p>Sed ut perspiciatis unde omnis iste natus error sit voluptatem accusantium doloremque laudantium, totam rem aperiam, eaque ipsa quae ab illo inventore veritatis et quasi architecto beatae vitae dicta sunt expli</p>
      <p>Aorem ipsum dolor sit amet, consectetur adipiscing elit, sed do eiusmod tempor incididunt ut labore et dolore magna liqua. Ut enim ad minim veniam, quis nostrud exercitation ullamco laboris nisi ut</p>
    </div>
    <div class="art" role="img" aria-label="Isometric illustration of analytics screens, laptop and magnifying glass" style="left:290px;top:597px;width:155px;height:154px;background:radial-gradient(ellipse at 50% 55%,#c9d6f5 0 30%,#eef2fc 60%,#fff 80%)"></div>

    <svg class="footer-wave" style="top:820px" width="498" height="167" viewBox="0 0 498 167">
      <defs><linearGradient id="footA" x1="0" y1="0" x2="0" y2="1"><stop offset="0" stop-color="#184f9a"/><stop offset="1" stop-color="#0f67b5"/></linearGradient></defs>
      <path d="M0 27C50 6 110 -2 170 4C240 12 290 30 360 26C420 22 465 10 498 1V167H0Z" fill="url(#footA)"/>
    </svg>
    <div class="footer-brand brand" style="top:878px"><span class="brand-dot"></span><span class="brand-name">Northfold<br>Portfolio</span></div>
    <div class="footer-social" style="top:902px"><span></span><span></span><span></span><span></span></div>
    <span class="footer-divider" style="left:172px;top:851px"></span>
    <span class="footer-divider" style="left:265px;top:851px"></span>
    <span class="footer-divider" style="left:358px;top:851px"></span>
    <div class="footer-col" style="left:184px;top:879px"><h4>Navigation</h4><ul><li>Strategies</li><li>Monthly Updates</li><li>FAQ</li><li>Signup</li><li>Login</li></ul></div>
    <div class="footer-col" style="left:273px;top:879px"><h4>Resources</h4><ul><li>Careers</li><li>Leadership</li><li>Blog</li><li>Events</li><li>Press</li></ul></div>
    <div class="footer-col" style="left:366px;top:879px"><h4>Get in touch</h4><ul><li>Contact</li><li>Support</li><li>Partners</li><li>Join research panel</li></ul></div>
  </section>

  <!-- Blog listing page -->
  <section class="page page--listing">
    <svg class="abs" style="left:0;top:34px" width="498" height="190" viewBox="0 0 498 190">
      <defs><linearGradient id="heroB" x1="0" y1="0" x2="0" y2="1"><stop offset="0" stop-color="#f8fbfe"/><stop offset="1" stop-color="#e8f1f8"/></linearGradient></defs>
      <path d="M0 0H498V140C440 150 390 175 300 175C200 175 120 150 60 140C30 136 10 138 0 140Z" fill="url(#heroB)"/>
    </svg>
    <header class="site-header">
      <div class="brand"><span class="brand-dot"></span><span class="brand-name">Northfold<br>Portfolio</span></div>
      <span class="nav-link" style="left:178px">STRATEGIES</span>
      <span class="nav-link" style="left:231px">MONTHLY UPDATES</span>
      <span class="nav-link" style="left:303px">FAQ</span>
      <span class="btn btn--ghost">SIGN UP</span>
      <span class="btn btn--solid">LOGIN</span>
    </header>

    <h2 class="hero-title">Our Blog <strong>Articles</strong></h2>
    <p class="hero-sub">NorthfoldPortfolio.com uses market data, factoring<br>and backtesting to make data driven</p>
    <div class="art" role="img" aria-label="Isometric illustration of a laptop showing a blog page with desk items and a plant" style="left:233px;top:53px;width:211px;height:169px;background:radial-gradient(ellipse at 60% 50%,#9cc6ea 0 25%,#dbe9f6 50%,rgba(232,241,248,0) 75%)"></div>

    <div class="art" role="img" aria-label="Isometric illustration of a data dashboard platform with charts" style="left:50px;top:251px;width:197px;height:142px;border:1px solid var(--mist);background:radial-gradient(ellipse at 50% 50%,#1b4f8f 0 18%,#9cc3e6 32%,#eef5fb 60%,#f8fbfe 100%)"></div>
    <div class="date-pill" style="left:261px;top:253px;width:54px;height:11px;font-size:5.4px">05 SEP 2021</div>
    <h2 class="post-title" style="left:264px;top:270px;width:190px;font-size:10.4px">Sed ut perspiciatis unde omnis iste natus error sit voluptatem accusantium</h2>
    <div class="byline" style="left:264px;top:307px;font-size:6.4px">By Elias Brennard MD<span class="share"><span></span><span></span><span></span></span></div>
    <div class="copy" style="left:264px;top:326px;width:178px">
      <p>Aorem ipsum dolor sit amet, consectetur adipiscing elit, sed do eiusmod tempor incididunt ut labore et dolore magna liqua. Ut enim ad minim veniam, quis nostrud exercitation ullamco laboris nisi ut aliquip ex ea commodo consequat. Duis aute irure dolor in reprehenderit in voluptate velit</p>
    </div>

    <div class="copy" style="left:55px;top:410px;width:382px">
      <p>Aorem ipsum dolor sit amet, consectetur adipiscing elit, sed do eiusmod tempor incididunt ut labore et dolore magna liqua. Ut enim ad minim veniam, quis nostrud exercitation ullamco laboris nisi ut aliquip ex ea commodo consequat. Duis aute irure dolor in reprehenderit in voluptate velit esse cillum dolore eu fugiat</p>
      <p>Sed ut perspiciatis unde omnis iste natus error sit voluptatem accusantium doloremque laudantium, totam rem aperiam, eaque ipsa quae ab illo inventore veritatis et quasi architecto beatae vitae dicta sunt explicabo. Nemo enim ipsam voluptatem quia voluptas sit aspernatur aut odit aut fugit, sed quia consequuntur magni dolores eos qui ratione voluptatem sequi nesciunt. Neque porro quisquam est, qui dolorem ipsum quia dolor sit amet, consectetur,</p>
    </div>
    <h3 class="section-head" style="left:55px;top:511px;font-size:9.4px">Sed ut perspiciatis unde omnis iste</h3>
    <div class="copy" style="left:55px;top:531px;width:382px">
      <p>Aorem ipsum dolor sit amet, consectetur adipiscing elit, sed do eiusmod tempor incididunt ut labore et dolore magna liqua. Ut enim ad minim veniam, quis nostrud exercitation ullamco laboris nisi ut aliquip ex ea commodo consequat. Duis aute irure dolor in reprehenderit in voluptate velit esse cillum dolore eu fugiat</p>
      <p>Aorem ipsum dolor sit amet, consectetur adipiscing elit, sed do eiusmod tempor incididunt ut labore et dolore magna liqua. Ut enim ad minim veniam, quis nostrud exercitation ullamco laboris nisi ut aliquip ex ea commodo consequat. Duis aute irure dolor in reprehenderit in voluptate velit esse cillum dolore eu fugiat</p>
      <p>Sed ut perspiciatis unde omnis iste natus error sit voluptatem accusantium doloremque laudantium, totam rem aperiam, eaque ipsa quae ab illo inventore veritatis et quasi architecto beatae vitae dicta sunt explicabo. Nemo enim ipsam voluptatem quia voluptas sit aspernatur aut odit aut fugit, sed quia consequuntur magni dolores eos qui ratione voluptatem sequi nesciunt. Neque porro quisquam est, qui dolorem ipsum quia dolor sit amet, consectetur,</p>
      <p style="margin-top:8px">Aorem ipsum dolor sit amet, consectetur adipiscing elit, sed do eiusmod tempor incididunt ut labore et dolore magna liqua. Ut enim ad minim veniam, quis nostrud exercitation ullamco laboris nisi ut aliquip ex ea commodo consequat. Duis aute irure dolor in reprehenderit in voluptate velit esse cillum dolore eu fugiat</p>
      <p>Sed ut perspiciatis unde omnis iste natus error sit voluptatem accusantium doloremque laudantium, totam rem aperiam, eaque ipsa quae ab illo inventore veritatis et quasi architecto beatae vitae dicta sunt explicabo. Nemo enim ipsam voluptatem quia voluptas sit aspernatur aut odit aut fugit, sed quia consequuntur magni dolores eos qui ratione voluptatem sequi nesciunt. Neque porro quisquam est, qui dolorem ipsum quia dolor sit amet, consectetur,</p>
    </div>

    <svg class="footer-wave" style="top:793px" width="498" height="161" viewBox="0 0 498 161">
      <defs><linearGradient id="footB" x1="0" y1="0" x2="0" y2="1"><stop offset="0" stop-color="#184f9a"/><stop offset="1" stop-color="#1658a6"/></linearGradient></defs>
      <path d="M0 27C50 8 110 -2 170 5C240 14 290 28 360 22C420 17 465 8 498 0V161H0Z" fill="url(#footB)"/>
    </svg>
    <div class="footer-brand brand" style="top:852px"><span class="brand-dot"></span><span class="brand-name">Northfold<br>Portfolio</span></div>
    <div class="footer-social" style="top:877px"><span></span><span></span><span></span><span></span></div>
    <span class="footer-divider" style="left:172px;top:823px"></span>
    <span class="footer-divider" style="left:264px;top:823px"></span>
    <span class="footer-divider" style="left:357px;top:823px"></span>
    <div class="footer-col" style="left:184px;top:853px"><h4>Navigation</h4><ul><li>Strategies</li><li>Monthly Updates</li><li>FAQ</li><li>Signup</li><li>Login</li></ul></div>
    <div class="footer-col" style="left:273px;top:853px"><h4>Resources</h4><ul><li>Careers</li><li>Leadership</li><li>Blog</li><li>Events</li><li>Press</li></ul></div>
    <div class="footer-col" style="left:366px;top:853px"><h4>Get in touch</h4><ul><li>Contact</li><li>Support</li><li>Partners</li><li>Join research panel</li></ul></div>
  </section>
</div>
</body>
</html>
```